Design a styled business card for an intimacy and attachment psychologist

I am a Psychologist providing online therapy to patients across the United States. My work is interpersonal and emotion-focused, with an emphasis on the client-therapist relationship. My primary areas of work are very personal, including sexuality and gender, abuse and trauma, and grief and loss. My target audience will be adults of all ages 18+.
My business card should convey a warm and inviting feeling of professionalism that is also casual and comfortable.
The front should be fairly simple and professional, consisting of:
- My name, Dr. Rosalind Petrakis
- My title, Licensed Psycholigist
- My logo
On either the front or the back, my contact information should be listed:
- ros@drrospetrakis.example
- 555.014.7788
- drrospetrakis.example
On the rear, I would like a description of the areas that I specialize in. This can be formatted in any way that appears stylistically interesting.
Individual and Couples
Relationships and Infidelity
Sexual Health & Aging
Gender Identity & Sexual Orientation
Abuse and Trauma
Sexual Compulsivity & Addiction
Sexual Dysfunction
Target Market(s)
My target audience will be adults of all ages 18+.
Industry/Entity Type
Psychology
Contact Information for Business Card
The front should be fairly simple and professional, consisting of: - My name, Dr. Rosalind Petrakis - My title, Licensed Psycholigist - My logo On either the front or the back, my contact information should be listed: - ros@drrospetrakis.example - 555.014.7788 - drrospetrakis.example On the rear, I would like a description of the areas that I specialize in. This can be formatted in any way that appears stylistically interesting. Individual and Couples Relationships and Infidelity Sexual Health & Aging Gender Identity & Sexual Orientation Abuse and Trauma Sexual Compulsivity & Addiction Sexual Dysfunction
- Follow brand guide

```html
<!DOCTYPE html>
<html lang="en">
<head>
<meta charset="utf-8">
<title>Dr. Rosalind Petrakis — Business Card</title>
<link rel="stylesheet" href="https://fonts.googleapis.com/css2?family=Figtree:wght@400;600&display=swap">
<style>
  :root {
    --page-bg: #eaf4f1;
    --card-bg: #d1ebe6;
    --ink: #2b2752;
    --mark-fill: #5fc4ad;
    --mark-line: #2b2752;
    --accent: #f5a623;
  }
  * { margin: 0; padding: 0; box-sizing: border-box; }
  html, body {
    width: 1199px; height: 1200px; overflow: hidden;
    background: var(--page-bg);
    font-family: "Figtree", sans-serif;
    color: var(--ink);
  }
  .card {
    position: absolute;
    left: 166px;
    width: 868px;
    height: 512px;
    background: var(--card-bg);
  }
  .card--front { top: 69px; }
  .card--back { top: 621px; }

  .identity { position: absolute; left: 58px; top: 244px; }
  .identity__name { font-size: 27px; font-weight: 600; line-height: 1.2; }
  .identity__title { font-size: 19px; font-weight: 400; margin-top: 8px; }

  .contact { position: absolute; left: 58px; top: 348px; list-style: none; }
  .contact__item {
    display: flex; align-items: center; gap: 10px;
    font-size: 19px; line-height: 33px;
  }
  .contact__icon { width: 17px; height: 17px; fill: var(--ink); flex: none; }

  .brand-mark {
    position: absolute;
    display: flex; flex-direction: column; align-items: center;
  }
  .brand-mark__dot {
    border-radius: 50%;
    background: var(--mark-fill);
    border: 6px solid var(--mark-line);
  }
  .brand-mark__name { font-weight: 600; color: var(--ink); white-space: nowrap; line-height: 1.2; }

  .card--front .brand-mark { left: 480px; top: 72px; width: 330px; }
  .card--front .brand-mark__dot { width: 240px; height: 240px; }
  .card--front .brand-mark__name { font-size: 26px; margin-top: 22px; }

  .card--back .brand-mark { left: 0; right: 0; top: 40px; }
  .card--back .brand-mark__dot { width: 130px; height: 130px; border-width: 5px; }
  .card--back .brand-mark__name { font-size: 40px; margin-top: 20px; }

  .specialties {
    position: absolute;
    left: 110px; right: 110px; top: 290px;
    display: grid;
    grid-template-columns: 1fr 1fr;
    column-gap: 40px;
    list-style: none;
    border-top: 2px solid var(--ink);
    padding-top: 22px;
  }
  .specialties__item {
    display: flex; align-items: center; gap: 10px;
    font-size: 18px; line-height: 34px;
    white-space: nowrap;
  }
  .specialties__item::before {
    content: "";
    width: 8px; height: 8px; border-radius: 50%;
    background: var(--accent);
    flex: none;
  }
</style>
</head>
<body>
  <section class="card card--front">
    <div class="identity">
      <h1 class="identity__name">Dr. Rosalind Petrakis</h1>
      <p class="identity__title">Licensed Psycholigist</p>
    </div>
    <ul class="contact">
      <li class="contact__item">
        <svg class="contact__icon" viewBox="0 0 24 24"><path d="M6.6 10.8a15.1 15.1 0 0 0 6.6 6.6l2.2-2.2c.3-.3.7-.4 1-.2 1.1.4 2.3.6 3.6.6.6 0 1 .4 1 1V20c0 .6-.4 1-1 1A17 17 0 0 1 3 4c0-.6.4-1 1-1h3.5c.6 0 1 .4 1 1 0 1.3.2 2.5.6 3.6.1.3 0 .7-.2 1z"/></svg>
        555.014.7788
      </li>
      <li class="contact__item">
        <svg class="contact__icon" viewBox="0 0 24 24"><path d="M2 5h20v14H2z M3.5 6.5 12 13l8.5-6.5" fill="none" stroke="#2b2752" stroke-width="2"/><path d="M2 5h20v1.5L12 13 2 6.5z"/></svg>
        ros@drrospetrakis.example
      </li>
      <li class="contact__item">
        <svg class="contact__icon" viewBox="0 0 24 24"><circle cx="12" cy="12" r="9.5" fill="none" stroke="#2b2752" stroke-width="2"/><path d="M12 2.5v19M2.5 12h19M12 2.5c-3.5 3-3.5 16 0 19M12 2.5c3.5 3 3.5 16 0 19" fill="none" stroke="#2b2752" stroke-width="1.5"/></svg>
        drrospetrakis.example
      </li>
    </ul>
    <div class="brand-mark">
      <span class="brand-mark__dot"></span>
      <span class="brand-mark__name">Rosalind Petrakis</span>
    </div>
  </section>

  <section class="card card--back">
    <div class="brand-mark">
      <span class="brand-mark__dot"></span>
      <span class="brand-mark__name">Dr. Rosalind Petrakis</span>
    </div>
    <ul class="specialties">
      <li class="specialties__item">Individual and Couples</li>
      <li class="specialties__item">Gender Identity &amp; Sexual Orientation</li>
      <li class="specialties__item">Relationships and Infidelity</li>
      <li class="specialties__item">Abuse and Trauma</li>
      <li class="specialties__item">Sexual Health &amp; Aging</li>
      <li class="specialties__item">Sexual Compulsivity &amp; Addiction</li>
      <li class="specialties__item">Sexual Dysfunction</li>
    </ul>
  </section>
</body>
</html>
```